VelmoraHub

Hey

I am involved with crowd funding, please look at one of my current sites www.funsprell.com
Work is currently under way with a new site www.velmorahub.com .wehave the basics but I am not happy with what we have so far. I need to redesign the web site but keep the concept . The cartoon pitch will be kept , along with some of the other functions which we can help you with, unless you are able to build / design something better. I liked a lot of the designs submitted for a previous crowd funning design, far better than what I currently have. To be included on this site will be links to numerous crowd funding sites which I have registered but each site will be focused on a specific topic which will be disclosed once this site is active. I intend to build all these sites through this site. Along with these sites will be a logo design for each site so plenty of work going forward. I have a logo for velmorahub already but am open for improvements and suggestions but would like to keep a map or logo of Africa included in the design. To bear in mind this is a African focused buisness which aims to help communities, employment creation, poverty alleviation and help young entrepreneurs kickstarter their buisness . I already have a group logo , which was designed on this site ( look at tandel yards competition) , I would like this logo to be used on all the site so customers and investors link the group and concept togeather. Here is the link http://www.brievoshop.co.uk/project-progress.aspx?briefId=48213 . I have removed the tandelyard from the bottom of the logo and will just be using the figurines as the group logo on all web sites. There will be at least fifty related crowd fund projects linked to this site.
If any body has any questions or ideas please feel free to ask for anything you may need. Thanks to everybody who helps with this project. Warmly. Ravi

Hi everyone working on my design.

The contact details to use on the site are

27 Weltmore Close
Dunvale
Cape Town 
+263748395026
+447913462058

E mail enquiries@VelmoraHub.example

There are two logos, one is the velmorahub logo and the other is my group logo which I will attach to the pitch
Good luck and thank you to everybody who is working on this web design
Warmly

Ravi

```html
<!DOCTYPE html>
<html lang="en">
<head>
<meta charset="utf-8">
<title>VelmoraHub – Crowdfunding Home</title>
<link href="https://fonts.googleapis.com/css2?family=Ubuntu:wght@300;400;500&family=Noto+Serif&display=swap" rel="stylesheet">
<style>
:root{
  --page:#f4f4f4;
  --panel:#f1f1f1;
  --border:#cfcfcf;
  --text:#555;
  --dark:#333;
  --blue:#2a6fc2;
  --blue-deep:#1d55a3;
  --blue-light:#3f8fd8;
  --orange:#e8662a;
  --orange-light:#f08a4a;
  --green:#4a9c34;
  --green-light:#6dbb4c;
  --title:#1a7fc1;
  --footer:#333;
}
*{box-sizing:border-box;margin:0;padding:0}
html,body{width:1029px;height:1200px;overflow:hidden;background:var(--page)}
body{font-family:"Ubuntu",sans-serif;color:var(--text)}
.stage{position:relative;width:1200px;height:1400px;transform:scale(.8575);transform-origin:0 0;background:#fafafa}
.abs{position:absolute}
.header{left:0;top:0;width:1200px;height:141px;background:linear-gradient(#ececec,#fafafa)}
.brand{left:130px;top:34px;display:flex;align-items:center;gap:8px;font-size:22px;color:var(--title);font-weight:400}
.brand-dot{width:22px;height:22px;border-radius:50%;background:var(--green)}
.utility{left:770px;top:12px;width:300px;height:33px;border-radius:4px;background:#6d6d6d;color:#fff;font-size:12.5px;display:flex;align-items:center;justify-content:center;gap:7px}
.field{top:68px;width:178px;height:29px;border:1px solid #bbb;border-radius:5px;background:#ededed;font-size:12.5px;color:#888;padding:7px 13px}
.account-links{left:827px;top:111px;font-size:12.5px;color:#888}
.account-links .register{color:#c0391b;font-weight:500}
.login{left:1000px;top:107px;width:70px;height:24px;border-radius:3px;background:linear-gradient(var(--green-light),var(--green));color:#fff;font-size:13px;font-weight:500;text-align:center;line-height:24px}
.nav{left:0;top:141px;width:1200px;height:44px;background:linear-gradient(var(--blue-light),var(--blue-deep))}
.nav a{position:absolute;top:14px;color:#fff;font-size:14.5px;font-weight:500;text-decoration:none}
.nav .home{left:130px;top:9px;width:80px;height:27px;border-radius:3px;background:linear-gradient(var(--orange-light),var(--orange));text-align:center;line-height:27px}
.slider{left:130px;top:192px;width:700px;height:345px;border:1px solid var(--border);border-radius:4px;overflow:hidden;background:radial-gradient(ellipse at 55% 40%,#f6f6f6,#c9ccd0 70%,#b5b8bd)}
.slider svg{position:absolute;top:152px}
.promo{left:850px;width:220px;height:164px;border:1px solid var(--border);border-radius:4px;background:var(--panel);overflow:hidden}
.promo h2{height:37px;background:linear-gradient(#555,#2c2c2c);color:#fff;font-size:24px;font-weight:500;text-align:center;line-height:38px}
.promo p{padding:6px 14px;font-size:12.5px;line-height:23px;text-align:center;font-weight:300;color:#555}
.box{border:1px solid var(--border);border-radius:4px;background:var(--panel)}
.cat-head{left:140px;top:576px;width:201px;height:30px;border-radius:3px;background:linear-gradient(var(--orange-light),var(--orange));color:#fff;font-size:14px;font-weight:500;padding:7px 13px}
.cats{left:153px;top:617px;list-style:none;font-size:13.5px;color:#444;line-height:19.5px}
.cats li{position:relative;padding-left:15px;margin-bottom:5.5px}
.cats li::before{content:"";position:absolute;left:0;top:7px;width:6px;height:6px;border-radius:50%;background:#f0a060}
.badge{border-radius:8px;background:#dcdcdc}
.follow{left:130px;top:1205px;font-size:18px;font-weight:500;color:var(--title)}
.social{top:1241px;width:32px;height:32px;border-radius:5px;background:#8a8f96;display:flex;align-items:center;justify-content:center}
.project{left:370px;width:700px;height:239px}
.project-head{height:39px;border-radius:4px 4px 0 0;background:linear-gradient(var(--green-light),var(--green));color:#fff;font-size:19px;font-weight:500;padding:8px 14px}
.project-photo{position:absolute;left:28px;top:62px;width:191px;height:153px}
.project-copy{position:absolute;left:240px;top:57px;width:440px;font-size:12.5px;line-height:23px;font-weight:300;color:#555}
.stats{position:absolute;left:243px;top:141px;display:flex;align-items:center;font-family:"Noto Serif",serif;font-size:17.5px;color:#333;height:34px}
.stats .count{font-size:28px;margin:0 14px 0 10px;font-family:"Ubuntu",sans-serif;font-weight:300}
.stats .sep{margin:0 18px}
.region{position:absolute;left:560px;top:141px;width:119px;height:33px;border-radius:3px;background:linear-gradient(var(--blue-light),var(--blue-deep));color:#fff;font-size:15px;font-weight:500;text-align:center;line-height:33px}
.footer{left:0;top:1329px;width:1200px;height:71px;background:var(--footer);color:#ddd;font-size:11.5px;text-align:center;line-height:70px}
</style>
</head>
<body>
<div class="stage">
  <div class="abs header"></div>
  <div class="abs brand"><span class="brand-dot"></span>TandelYards</div>
  <div class="abs utility"><span>Join Now</span>|<span>How it Works</span>|<span>Browse Companies</span></div>
  <div class="abs field" style="left:695px">Username</div>
  <div class="abs field" style="left:893px">Password</div>
  <div class="abs account-links"><span class="register">Register</span> &nbsp;|&nbsp; Fogot Password?</div>
  <div class="abs login">Log In</div>

  <nav class="abs nav">
    <a class="home" href="#">Home</a>
    <a href="#" style="left:247px">About Us</a>
    <a href="#" style="left:355px">How it Works</a>
    <a href="#" style="left:490px">Blog</a>
    <a href="#" style="left:568px">IPO’s</a>
    <a href="#" style="left:649px">More @ VelmoraHub</a>
    <a href="#" style="left:841px">My Account</a>
    <a href="#" style="left:990px">My Cart</a>
  </nav>

  <div class="abs slider" role="img" aria-label="Group of smiling business people in suits standing in front of a faint world map">
    <svg style="left:10px" width="28" height="44" viewBox="0 0 28 44"><path d="M22 4 6 22l16 18" fill="none" stroke="#2a5fb0" stroke-width="7" stroke-linecap="round" stroke-linejoin="round"/></svg>
    <svg style="left:660px" width="28" height="44" viewBox="0 0 28 44"><path d="M6 4l16 18L6 40" fill="none" stroke="#2a5fb0" stroke-width="7" stroke-linecap="round" stroke-linejoin="round"/></svg>
  </div>

  <div class="abs promo" style="top:192px"><h2>FUND</h2><p>The elephant with no trunk. They say that a picture paints a thou­sand words, but no words can describe the pain, the anguish and the… »</p></div>
  <div class="abs promo" style="top:373px"><h2>JOIN</h2><p>The elephant with no trunk. They say that a picture paints a thou­sand words, but no words can describe the pain, the anguish and the… »</p></div>

  <div class="abs box" style="left:130px;top:562px;width:221px;height:343px"></div>
  <div class="abs cat-head">BUSINESS CATEGORIES</div>
  <ul class="abs cats">
    <li>Comics</li><li>Environment</li><li>Fashion</li><li>Film &amp; Video</li><li>Gaming</li><li>Health &amp; Fitness</li>
    <li>Internet, IT &amp;<br>Telecommunications</li><li>Leisure &amp; Tourism</li><li>Music</li><li>Professional Services</li><li>Technology</li>
  </ul>

  <div class="abs box" style="left:130px;top:926px;width:221px;height:231px"></div>
  <div class="abs badge" style="left:148px;top:945px;width:185px;height:58px;border-radius:29px 6px 6px 29px"></div>
  <div class="abs badge" style="left:193px;top:1027px;width:95px;height:37px;border-radius:19px"></div>
  <div class="abs badge" style="left:179px;top:1095px;width:122px;height:38px;border-radius:4px"></div>

  <div class="abs follow">Follow Us on:</div>
  <div class="abs social" style="left:130px"></div>
  <div class="abs social" style="left:172px"></div>
  <div class="abs social" style="left:213px">
    <svg width="18" height="18" viewBox="0 0 18 18" fill="#fff"><circle cx="4" cy="9" r="2.6"/><circle cx="14" cy="4" r="2.6"/><circle cx="14" cy="14" r="2.6"/><path d="M4 9 14 4M4 9l10 5" stroke="#fff" stroke-width="1.6"/></svg>
  </div>
  <div class="abs social" style="left:256px"></div>
  <div class="abs social" style="left:299px">
    <svg width="20" height="14" viewBox="0 0 20 14"><rect x="1" y="1" width="18" height="12" rx="1.5" fill="#fff"/><path d="M1.5 1.5 10 8l8.5-6.5" fill="none" stroke="#8a8f96" stroke-width="1.5"/></svg>
  </div>

  <section class="abs box project" style="top:562px">
    <div class="project-head">Ut placerat nunc suscipit</div>
    <div class="project-photo" role="img" aria-label="Pale blue hydrangea flower among dark green leaves" style="background:radial-gradient(circle at 50% 45%,#c9d3cf,#6d8f52 45%,#1f3a1a)"></div>
    <p class="project-copy">Ut placerat nunc suscipit metus lacinia vel interdum tortor eleifend. Aliquam erat volutpat. Ut consectetur auctor ornare. Donec molestie eros id lacus porta tempus. Phasellus… &nbsp;»</p>
    <div class="stats"><svg width="26" height="24" viewBox="0 0 26 24" fill="#1c7fc4"><circle cx="6" cy="5" r="3.5"/><circle cx="20" cy="5" r="3.5"/><circle cx="13" cy="7" r="4"/><rect x="2" y="9" width="8" height="12" rx="3"/><rect x="16" y="9" width="8" height="12" rx="3"/><rect x="8.5" y="12" width="9" height="12" rx="3"/></svg><span class="count">0</span>Funded $0<span class="sep">|</span>Goal $1,000</div>
    <div class="region">Russia</div>
  </section>

  <section class="abs box project" style="top:819px">
    <div class="project-head">Proin in ante et nulla</div>
    <div class="project-photo" role="img" aria-label="Three penguins standing on a beach under a blue sky" style="background:linear-gradient(#8fb0d8,#b9c9d8 55%,#7c858e)"></div>
    <p class="project-copy">Proin in ante et nulla mollis faucibus non sit amet felis. Vestibulum ac eros risus. Nullam turpis orci, ornare vitae porta vitae, fringilla vitae sem.</p>
    <div class="stats"><svg width="26" height="24" viewBox="0 0 26 24" fill="#1c7fc4"><circle cx="6" cy="5" r="3.5"/><circle cx="20" cy="5" r="3.5"/><circle cx="13" cy="7" r="4"/><rect x="2" y="9" width="8" height="12" rx="3"/><rect x="16" y="9" width="8" height="12" rx="3"/><rect x="8.5" y="12" width="9" height="12" rx="3"/></svg><span class="count">0</span>Funded $0<span class="sep">|</span>Goal $500</div>
    <div class="region">Middle East</div>
  </section>

  <section class="abs box project" style="top:1076px">
    <div class="project-head">Ut placerat nunc suscipit</div>
    <div class="project-photo" role="img" aria-label="Pale blue hydrangea flower among dark green leaves" style="background:radial-gradient(circle at 50% 45%,#c9d3cf,#6d8f52 45%,#1f3a1a)"></div>
    <p class="project-copy">Ut placerat nunc suscipit metus lacinia vel interdum tortor eleifend. Aliquam erat volutpat. Ut consectetur auctor ornare. Donec molestie eros id lacus porta tempus. Phasellus… &nbsp;»</p>
    <div class="stats"><svg width="26" height="24" viewBox="0 0 26 24" fill="#1c7fc4"><circle cx="6" cy="5" r="3.5"/><circle cx="20" cy="5" r="3.5"/><circle cx="13" cy="7" r="4"/><rect x="2" y="9" width="8" height="12" rx="3"/><rect x="16" y="9" width="8" height="12" rx="3"/><rect x="8.5" y="12" width="9" height="12" rx="3"/></svg><span class="count">0</span>Funded $0<span class="sep">|</span>Goal $1,000</div>
    <div class="region">Russia</div>
  </section>

  <footer class="abs footer">Copyright 2012 VelmoraHub</footer>
</div>
</body>
</html>
```